Quorvel Properties - Chat n’ Clink Evening Graphic Invite

We need a graphic design for a corporate reception that we are calling Chat n’ Clink Evening. The invite should read:

"QVR invites you to join us at Chat n’ Clink Evening

Monday, Jan 22nd
6:30 - 8:30 pm EST

Tallow Grill - Lounge Room

48213 E Harrow Glen Rd
Aventura, FL 33417

Join us for excellent wine and tasty bites at our semi-annual PDA reception. Swing by whenever you can – timing is casual and we'd love to see you there!"

Please feel free to use fun photos from the Tallow Grill gallery: https://www.tallowgrillexample.com/photos

Also, please use the QVR logo attached.

Target Market(s)

Corporate professional

Colors
0054AA
0677BA
7BADD7
CADEEF
E8F1F8

Requirements
Must have
• QVR logo, attached verbiage

```html
<!DOCTYPE html>
<html lang="en">
<head>
<meta charset="utf-8">
<title>QVR – Chat n’ Clink Evening Invite</title>
<link href="https://fonts.googleapis.com/css2?family=Playfair+Display:ital,wght@1,600&family=Zilla+Slab:wght@400;500&display=swap" rel="stylesheet">
<style>
  :root {
    --backdrop-warm: #6b4a2c;
    --backdrop-light: #c9b79c;
    --backdrop-deep: #2b1c12;
    --panel: rgba(28, 22, 18, 0.78);
    --ink: #f3eee6;
    --ink-soft: #ddd6cb;
    --accent: #f0c419;
    --rule: #e9e3da;
  }
  * { margin: 0; padding: 0; box-sizing: border-box; }
  html, body { width: 846px; height: 1200px; overflow: hidden; background: #ffffff; }
  .invite {
    position: relative;
    width: 846px;
    height: 1200px;
    overflow: hidden;
    font-family: "Zilla Slab", Georgia, serif;
    color: var(--ink);
  }
  .venue-photo {
    position: absolute;
    inset: 0;
    background:
      radial-gradient(ellipse at 50% 10%, var(--backdrop-light) 0%, transparent 45%),
      linear-gradient(180deg, #a89276 0%, var(--backdrop-warm) 40%, #4a3220 70%, var(--backdrop-deep) 100%);
  }
  .panel {
    position: absolute;
    left: 73px;
    top: 73px;
    width: 700px;
    height: 1055px;
    background: var(--panel);
    text-align: center;
  }
  .brand {
    position: absolute;
    top: 105px;
    left: 0;
    right: 0;
    display: flex;
    justify-content: center;
    align-items: center;
    gap: 14px;
    font-family: "Zilla Slab", Georgia, serif;
    font-weight: 500;
    font-size: 46px;
    letter-spacing: 2px;
    color: var(--ink);
  }
  .brand-mark {
    width: 30px;
    height: 30px;
    background: var(--ink);
  }
  .invites-line {
    position: absolute;
    top: 208px;
    left: 0; right: 0;
    font-size: 23px;
    color: var(--ink-soft);
  }
  .event-title {
    position: absolute;
    top: 250px;
    left: 0; right: 0;
    font-family: "Playfair Display", Georgia, serif;
    font-style: italic;
    font-weight: 600;
    font-size: 98px;
    line-height: 108px;
    color: var(--ink);
  }
  .details {
    position: absolute;
    top: 540px;
    left: 0; right: 0;
    font-size: 26px;
    line-height: 33px;
  }
  .details .venue-gap { margin-top: 14px; }
  .venue-name { color: var(--accent); font-weight: 500; }
  .join-heading {
    position: absolute;
    top: 735px;
    left: 80px;
    right: 80px;
    display: flex;
    align-items: center;
    gap: 26px;
    font-size: 27px;
  }
  .join-heading::before, .join-heading::after {
    content: "";
    flex: 1;
    height: 2px;
    background: var(--rule);
  }
  .join-copy {
    position: absolute;
    top: 776px;
    left: 0; right: 0;
    font-size: 26px;
    line-height: 36px;
  }
  .divider {
    position: absolute;
    top: 858px;
    left: 80px;
    width: 540px;
    height: 2px;
    background: var(--rule);
  }
  .casual-note {
    position: absolute;
    top: 878px;
    left: 0; right: 0;
    font-size: 20px;
    line-height: 29px;
    color: var(--ink-soft);
  }
</style>
</head>
<body>
  <main class="invite">
    <div class="venue-photo" role="img" aria-label="Photo of the Tallow Grill lounge dining room with warm lighting, tables and upholstered chairs"></div>

    <section class="panel">
      <div class="brand"><span class="brand-mark"></span><span>QVR</span></div>

      <p class="invites-line">QVR Invites you to join us at</p>

      <h1 class="event-title">Chat n’ Clink<br>Evening</h1>

      <div class="details">
        <p>Monday, Jan 22nd, 2024</p>
        <p>6:30-8:30pm Est</p>
        <p class="venue-gap"><span class="venue-name">@ Tallow Grill</span> - Lounge Room</p>
        <p>48213 E Harrow Glen Rd</p>
        <p>Aventura, FL 33417</p>
      </div>

      <p class="join-heading">Join us</p>

      <p class="join-copy">for Excellent Wine and Tasty Bites<br>at our Semi-Annual PDA Reception</p>

      <div class="divider"></div>

      <p class="casual-note">Swing by whenever you can -<br>Timing is Casual<br>and we’d love to see you</p>
    </section>
  </main>
</body>
</html>
```